BOLD Gym Needs a New WALL WRAP!

We have a small wall that we need to spice up and we'd like to wrap it with a bold design that stands out and breaks up the current bland grey color.
The wall itself is 128.25" long x 50.5" tall
I am open to design options, but the design must include our ZorvaLyft logo (attached)
I have also included photos of the gym to give you an idea of the vibe, colors, etc.
DO NOT BE AFRAID OF COLOR😊​ Although our colors are Yellow, Grey's, Blacks, etc., in the gym, please do not be afraid to play with color while still making it look like it belongs in our building. The posters that hang around that wall have pinks, purples, etc. in it. I've included a poster for you to see the colors that are nearby.
The photo from the ground looking up towards the second story highlights the wall that needs to be wrapped.
The ultimate goal here is to break up the grey wall with a killer design.

```html
<!DOCTYPE html>
<html lang="en">
<head>
<meta charset="utf-8">
<title>ZorvaLyft Wall Wrap</title>
<link rel="stylesheet" href="https://fonts.googleapis.com/css2?family=Montserrat:wght@700;800;900&display=swap">
<style>
  :root {
    --board: #333333;
    --ink-black: #000000;
    --stripe-1: #231f20;
    --stripe-2: #414042;
    --stripe-3: #58595b;
    --stripe-4: #6d6e71;
    --brand-yellow: #f8d000;
    --white: #ffffff;
  }
  html, body {
    margin: 0;
    padding: 0;
    width: 1200px;
    height: 780px;
    overflow: hidden;
    background: var(--board);
  }
  .presentation { display: block; width: 1200px; height: 780px; }
  .headline { font-family: "Montserrat", sans-serif; font-weight: 700; font-size: 49px; }
  .headline .accent { fill: var(--brand-yellow); }
  .headline .lead { fill: var(--white); }
  .brand-name { font-family: "Montserrat", sans-serif; font-weight: 900; fill: var(--white); }
  .fill-yellow { fill: var(--brand-yellow); }
  .fill-white { fill: var(--white); }
  .fill-dark { fill: var(--stripe-1); }
</style>
</head>
<body>
<svg class="presentation" viewBox="0 0 1200 780" xmlns="http://www.w3.org/2000/svg">
  <defs>
    <radialGradient id="photo-tone" cx="0.5" cy="0.45" r="0.6">
      <stop offset="0" stop-color="#4a4a4a"/>
      <stop offset="0.6" stop-color="#1c1c1c"/>
      <stop offset="1" stop-color="#0a0a0a"/>
    </radialGradient>
  </defs>

  <g class="wall-wrap">
    <rect class="canvas-black" x="165" y="87" width="869" height="343" fill="var(--ink-black)"/>

    <g class="grey-stripes">
      <rect x="165" y="87" width="80" height="343" fill="var(--stripe-1)"/>
      <rect x="245" y="87" width="81" height="343" fill="var(--stripe-2)"/>
      <rect x="326" y="87" width="80" height="343" fill="var(--stripe-3)"/>
      <rect x="406" y="87" width="81" height="343" fill="var(--stripe-4)"/>
    </g>

    <rect class="athlete-photo" x="776" y="87" width="258" height="343" fill="url(#photo-tone)"
          role="img" aria-label="Black and white photo of a muscular athlete curling a barbell"/>

    <g class="yellow-corners">
      <polygon class="fill-yellow" points="354,87 517,87 517,211 456,211"/>
      <polygon class="fill-yellow" points="165,301 266,301 266,350 165,430"/>
      <polygon class="fill-yellow" points="936,353 972,353 1034,430 936,430"/>
    </g>

    <g class="accent-bars-white fill-white">
      <rect x="214" y="133" width="38" height="11" transform="rotate(-40 233 138)"/>
      <rect x="216" y="150" width="64" height="12" transform="rotate(-40 248 156)"/>
      <rect x="222" y="165" width="70" height="11" transform="rotate(-40 257 170)"/>
    </g>

    <g class="accent-bars-dark fill-dark">
      <rect x="285" y="333" width="92" height="22" transform="rotate(-42 331 344)"/>
      <rect x="313" y="357" width="74" height="22" transform="rotate(-42 350 368)"/>
      <rect x="345" y="368" width="40" height="11" transform="rotate(-42 365 374)"/>
    </g>

    <g class="accent-bars-yellow fill-yellow">
      <rect x="411" y="313" width="17" height="87" transform="rotate(2 420 356)"/>
      <rect x="435" y="322" width="16" height="69"/>
      <rect x="460" y="339" width="11" height="35"/>
    </g>

    <text class="brand-name" x="325" y="277" font-size="40" text-anchor="middle">ZorvaLyft</text>

    <g class="headline">
      <text x="541" y="222" textLength="333" lengthAdjust="spacing"><tspan class="lead">P</tspan><tspan class="accent">ERSO</tspan><tspan class="lead">N</tspan><tspan class="accent">AL</tspan></text>
      <text class="accent" x="601" y="274" textLength="216" lengthAdjust="spacing">GROUP</text>
      <text x="555" y="329" textLength="309" lengthAdjust="spacing"><tspan class="lead">T</tspan><tspan class="accent">RAINI</tspan><tspan class="lead">N</tspan><tspan class="accent">G</tspan></text>
    </g>

    <g class="headline-rules fill-white">
      <rect x="542" y="188" width="9" height="67"/>
      <rect x="780" y="145" width="9" height="77"/>
      <rect x="565" y="295" width="9" height="79"/>
      <rect x="784" y="295" width="9" height="79"/>
    </g>
  </g>

  <text class="brand-name" x="600" y="652" font-size="72" text-anchor="middle">ZorvaLyft</text>
</svg>
</body>
</html>
```